Business Card Design Project : Tidewell Press

In preparation for market launch, Whistler's Tidewell Press require the development of a business card. Tidewell Press is a Community online publishing web portal. We provide the the city of Whistler located in B.C. (Canada) business directories, News, Classified ads, News, Events and blogs etc.

The main focus of the brand is to help local businesses to corporate with their online advertisement and marketing. Meeting our clients face to face is a must (B2B).

Target Market(s)

The target market is B2B customers. Business Owners to Marketing, advertising Managers

Industry/Entity Type

Business

Requirements
Must have
• - The business card will be two sided.
the BACK side will have our logo which consist of (icon, url,slogan) submited. The logo will be middle and centred.

The FRONT side should have company details:

Company Legal Name: FERNDALE TIDEWELL PRESS

Owen Marsk
Director of Sales & Marketing

www.ferndaletidewell.biz
owen@ferndaletidewell.biz

Phone: 555 014 3826
#2817 - 562 E. Harlow Ave.
Vancouver, B.C. K7P2R4 Canada
Nice to have
• - For the "FRONT" side of our business card. You can separate or re-arrange with our logo components (icon, logo,slogan). It does not have to be together.

Also our company legal name is rather long so arrange or organize the name in a way to make it shorter. Your experience and creativity will have to come in play.
Should not have
• should not have other colors beside logo color and black text (2 colors). Also nothing Three dimensional

```html
<!DOCTYPE html>
<html lang="en">
<head>
<meta charset="utf-8">
<title>Ferndale Tidewell Press — Business Card</title>
<link rel="stylesheet" href="https://fonts.googleapis.com/css2?family=Lobster&family=Orbitron:wght@400&family=Saira+Semi+Condensed:wght@600&family=Arimo:wght@700&family=Open+Sans:wght@400;600;700&display=swap">
<style>
  :root {
    --brand-blue: #0a7fd0;
    --ink: #111111;
    --paper: #ffffff;
    --backdrop: #eceef1;
  }
  * { margin: 0; padding: 0; box-sizing: border-box; }
  html, body {
    width: 940px;
    height: 1200px;
    overflow: hidden;
    background: var(--backdrop);
  }
  .sheet {
    position: relative;
    width: 940px;
    height: 1200px;
  }
  .card {
    position: absolute;
    left: 32px;
    width: 876px;
    height: 500px;
    overflow: hidden;
    background: var(--paper);
  }
  .card--front { top: 40px; background: var(--brand-blue); }
  .card--back  { top: 640px; }

  .front-sweep {
    position: absolute;
    inset: 0;
    width: 876px;
    height: 500px;
  }
  .company-name {
    position: absolute;
    top: 46px;
    right: 32px;
    font-family: "Saira Semi Condensed", sans-serif;
    font-weight: 600;
    font-size: 35px;
    letter-spacing: 1px;
    color: var(--paper);
    white-space: nowrap;
  }
  .person-name {
    position: absolute;
    left: 78px;
    top: 168px;
    font-family: "Lobster", cursive;
    font-size: 58px;
    line-height: 1;
    color: var(--ink);
  }
  .person-title {
    position: absolute;
    left: 78px;
    top: 244px;
    font-family: "Orbitron", sans-serif;
    font-size: 13px;
    letter-spacing: 2.6px;
    color: var(--paper);
    text-transform: uppercase;
  }
  .online-contact {
    position: absolute;
    left: 78px;
    top: 364px;
    font-family: "Arimo", sans-serif;
    font-weight: 700;
    font-size: 17px;
    line-height: 24px;
    color: var(--ink);
  }
  .postal-contact {
    position: absolute;
    right: 28px;
    top: 402px;
    text-align: right;
    font-family: "Arimo", sans-serif;
    font-weight: 700;
    font-size: 17px;
    line-height: 23.5px;
    color: var(--brand-blue);
  }

  .brand-lockup {
    position: absolute;
    left: 0;
    right: 0;
    top: 150px;
    text-align: center;
  }
  .brand-mark {
    display: inline-flex;
    align-items: center;
    gap: 16px;
    font-family: "Open Sans", sans-serif;
    font-weight: 600;
    font-size: 50px;
    line-height: 1;
    color: var(--brand-blue);
  }
  .brand-mark__dot {
    width: 26px;
    height: 26px;
    border-radius: 50%;
    background: var(--brand-blue);
  }
  .brand-url {
    margin-top: 40px;
    font-family: "Open Sans", sans-serif;
    font-weight: 700;
    font-size: 38px;
    letter-spacing: -0.5px;
    line-height: 1.1;
    color: var(--ink);
  }
  .brand-slogan {
    font-family: "Open Sans", sans-serif;
    font-weight: 400;
    font-size: 28px;
    letter-spacing: -0.5px;
    line-height: 1.2;
    color: var(--brand-blue);
  }
</style>
</head>
<body>
<main class="sheet">

  <section class="card card--front" aria-label="Business card front">
    <svg class="front-sweep" viewBox="0 0 876 500" aria-hidden="true">
      <path d="M0,460 C300,450 480,420 600,360 C700,310 790,300 876,300 L876,500 L0,500 Z" fill="#ffffff"/>
    </svg>
    <div class="company-name">FERNDALE TIDEWELL PRESS</div>
    <h1 class="person-name">Owen Marsk</h1>
    <p class="person-title">Director of Sales &amp; Marketing</p>
    <p class="online-contact">
      www.ferndaletidewell.biz<br>
      owen@ferndaletidewell.biz
    </p>
    <p class="postal-contact">
      Phone: 555 014 3826<br>
      #2817 - 562 E. Harlow Ave.<br>
      Vancouver, B.C. K7P2R4 Canada
    </p>
  </section>

  <section class="card card--back" aria-label="Business card back">
    <div class="brand-lockup">
      <div class="brand-mark"><span class="brand-mark__dot"></span>Tidewell Press</div>
      <p class="brand-url">www.ferndaletidewell.biz</p>
      <p class="brand-slogan">Your information gateway</p>
    </div>
  </section>

</main>
</body>
</html>
```